Vantix 220 for iPad

We are looking to design a page for the mobile app. The app is intended for financial professionals and is based on a successful desktop application. The existing design will serve as a very rough guideline, but we are open to hearing ideas.
Uploaded file #1 contains a screenshot of the existing design. The workflow is as follows:
The user picks a portfolio from the Dropdown below portfolio.
The user picks a Loss Threshold, which will dictate what gets onto the bubble chart below.
Once the bubble on the chart is clicked, a text box pops up with the description of the particular crisis that the bubble represents.
Once the bubble is clicked, the right hand side bar charts are populated with moves relevant to this scenario.
The left hand pane contains two text boxes. The lower one is particularly important, because the user is able to remove scenarios or add scenarios (screen #2). Removing scenarios is simple.
Adding scenarios brings up a wizard (screen #3). It also needs to be designed consistently with the front page of the app. The wizard has different clickable categories going down the column on the left and in a row on the top. The user can pick some or all of these categories.

Notes: The app should be designed for landscape mode only. The key to keep in mind is how the user will select bubbles on the chart. Right now, it is quite easy, but with the touchscreen it may be more complicated, so please keep that in mind when designing the chart (it should still be some version of the similar chart).
*As a first pass, please submit your idea of the concept (layout/colors/buttons) without the detailed design. We will choose 1-3 concepts and then the detailed work will take place with a much higher chance of a payout.
Updates

Thank you for the first two sketches. The second one by bertrand appears to be a bit more mobile app oriented, though we are still considering both and waiting for other submissions. One request, could you rework the sketches to include a bit more of dark blue as a background?  \

Bertrand, I think that the bubbles are too small and they are missing some volume effects. Could you make them a bit more prominent (and pick some form of dark blue background) and change the color to see if they will stand out better?
 

Industry/Entity Type

Financial

Requirements
Must have
• The general outline for the bubble chart must be retained. But the actual execution may differ significantly. We are open to seeing different ideas.
The winning design will also get a contract to design the rest of the application (2 more screens), which will be worth the same as the original design.

```html
<!DOCTYPE html>
<html lang="en">
<head>
<meta charset="utf-8">
<title>Vantix 220</title>
<link href="https://fonts.googleapis.com/css2?family=Arimo:wght@400;700&family=Nunito:wght@800&display=swap" rel="stylesheet">
<style>
:root{
  --stage-top:#6e6e6e;--stage-mid:#8a8a8a;--stage-bottom:#000;
  --nav-dark:#1c1b1a;--nav-light:#4a4744;
  --app-blue:#0b4a8f;
  --yellow:#f5c518;--ink:#111;--white:#fff;
  --grid-bg:#e4e4e4;--grid-line:#fafafa;
  --green:#7cc242;--green-dark:#5aa02a;
  --red:#d9261c;--red-dark:#b41a12;
  --btn-top:#4b4845;--btn-bottom:#1e1d1c;
  --row-alt:#e2e2e2;--row-head:#c9c9c9;
}
*{margin:0;padding:0;box-sizing:border-box}
html,body{width:1200px;height:1000px;overflow:hidden}
body{font-family:"Arimo",Arial,sans-serif;background:linear-gradient(180deg,var(--stage-top) 0,var(--stage-mid) 55%,#3a3a3a 75%,var(--stage-bottom) 92%);position:relative}
.app{position:absolute;left:48px;top:90px;width:1100px;height:825px;background:var(--app-blue);
  background-image:repeating-linear-gradient(135deg,rgba(255,255,255,.03) 0 2px,transparent 2px 5px);}
.app-topstrip{position:absolute;left:0;top:0;width:100%;height:15px;background:#111}
.nav{position:absolute;left:0;top:15px;width:100%;height:43px;background:linear-gradient(180deg,var(--nav-light),var(--nav-dark));display:flex;color:var(--white);font-size:15px}
.nav-item{height:100%;display:flex;align-items:center;justify-content:center;border-right:1px solid #6a6662}
.nav-hints{margin-left:auto;width:180px;display:flex;align-items:center;justify-content:center}
.nav-dots{width:90px;display:flex;align-items:center;gap:13px;padding-left:12px}
.dot{width:16px;height:16px;border-radius:50%;background:#ddd}
.dot.active{background:#fff;border:3px solid #1e88e5}
.portfolio-select{position:absolute;left:30px;top:66px;width:655px;height:34px;background:var(--yellow);border-radius:4px;font-weight:700;font-size:19px;padding:6px 12px;color:var(--ink)}
.portfolio-select::after{content:"";position:absolute;right:12px;top:15px;border:5px solid transparent;border-top:6px solid #333}
.doc-btn{position:absolute;left:693px;top:66px;width:48px;height:34px;background:#f2f2f2;border-radius:4px}
.brand{position:absolute;left:827px;top:66px;font-family:"Nunito",Arial,sans-serif;font-weight:800;font-size:28px;color:var(--white)}
.controls{position:absolute;left:16px;top:107px;width:154px;color:var(--white);font-size:13px;text-align:center}
.ctl-label{display:block;height:18px;line-height:18px}
.ctl-btn{display:block;margin:2px auto 0;width:114px;height:34px;border-radius:4px;background:linear-gradient(180deg,var(--btn-top),var(--btn-bottom));box-shadow:0 2px 3px rgba(0,0,0,.5);font-weight:700;font-size:16px;line-height:34px;position:relative}
.ctl-btn.drop{text-align:left;padding-left:22px}
.ctl-btn.drop::after{content:"";position:absolute;right:8px;top:14px;border:5px solid transparent;border-top:6px solid #fff}
.checkbox{display:block;margin:5px auto 0;width:16px;height:16px;background:#fff;border:1px solid #999}
.search{position:absolute;left:16px;top:609px;width:159px;height:35px;background:#e6e6e6;border-radius:4px}
.chart{position:absolute;left:160px;top:100px}
.bars{position:absolute}
.bar-title{position:absolute;left:0;top:0;width:331px;height:25px;color:var(--white);font-weight:700;font-size:12.5px;text-align:center;line-height:25px;border-radius:5px 5px 0 0}
.table{position:absolute;top:673px;height:138px;border-radius:6px;overflow:hidden;background:#fff;font-size:15px;color:var(--ink)}
.table-title{height:26px;background:linear-gradient(180deg,#4a4744,#1c1b1a);color:var(--white);font-weight:700;font-size:13px;text-align:center;line-height:26px}
.row{display:flex;height:20.5px;line-height:20.5px}
.row.head{background:var(--row-head);height:28px;line-height:28px}
.row.alt{background:var(--row-alt)}
.row.selected{background:var(--yellow)}
.cell{padding-left:16px;border-right:2px solid #d0d0d0}
.cell.num{text-align:right;padding-right:30px;padding-left:0}
.cell.mid{text-align:center;padding-left:0}
</style>
</head>
<body>
<main class="app">
  <div class="app-topstrip"></div>
  <nav class="nav">
    <span class="nav-item" style="width:148px;justify-content:flex-end;padding-right:28px">New Tab</span>
    <span class="nav-item" style="width:134px">Current Tab</span>
    <span class="nav-item" style="width:132px">Saved Tab</span>
    <span class="nav-item" style="width:92px">Tools</span>
    <span class="nav-item" style="width:142px">Load models</span>
    <span class="nav-item" style="width:100px">About</span>
    <span class="nav-hints">? Hints</span>
    <span class="nav-dots"><span class="dot active"></span><span class="dot"></span><span class="dot"></span></span>
  </nav>

  <div class="portfolio-select">MAM AA</div>
  <div class="doc-btn"><svg width="48" height="34" viewBox="0 0 48 34"><path d="M15 7h13l5 5v16H15z" fill="#fff" stroke="#333" stroke-width="1.5"/><path d="M19 14h10M19 18h10M19 22h10" stroke="#333" stroke-width="1.5"/></svg></div>
  <div class="brand">Vantix 220</div>

  <section class="controls">
    <span class="ctl-label">Portfolio Date</span><span class="ctl-btn drop">6/18/2013</span>
    <span class="ctl-label" style="margin-top:20px">Currency</span><span class="ctl-btn drop">USD</span>
    <span class="ctl-label" style="margin-top:19px">Model Date 06/12/2013</span><span class="ctl-btn">Read Model</span>
    <span class="ctl-label" style="margin-top:20px">Weight Type</span><span class="ctl-btn drop">Active</span>
    <span class="ctl-label" style="margin-top:19px">Model</span><span class="ctl-btn drop" style="padding-left:14px">Quantora</span>
    <span class="ctl-label" style="margin-top:20px">Loss Threshold</span><span class="ctl-btn">-10</span>
    <span class="ctl-label" style="margin-top:12px">Online Key Scenarios</span><span class="checkbox"><svg width="14" height="14"><path d="M2 7l3 4 7-9" stroke="#d9261c" stroke-width="2.5" fill="none"/></svg></span>
    <span class="ctl-label" style="margin-top:8px">Current Scenario</span>
  </section>
  <div class="search"><svg width="159" height="35"><circle cx="138" cy="15" r="6" stroke="#555" stroke-width="2" fill="none"/><path d="M142 19l6 6" stroke="#555" stroke-width="2.5"/></svg></div>

  <svg class="chart" width="600" height="562" viewBox="0 0 600 562" font-family="Arimo,Arial,sans-serif">
    <defs>
      <pattern id="grid" width="22.1667" height="22.2917" patternUnits="userSpaceOnUse" x="50" y="10">
        <path d="M0 0V22.2917M0 0H22.1667" stroke="#fafafa" stroke-width="1" fill="none"/>
      </pattern>
      <radialGradient id="bRed" cx=".35" cy=".35"><stop offset="0" stop-color="#ff6a5a"/><stop offset="1" stop-color="#a50d08"/></radialGradient>
      <radialGradient id="bOrange" cx=".35" cy=".35"><stop offset="0" stop-color="#ffe25a"/><stop offset="1" stop-color="#e2570c"/></radialGradient>
      <radialGradient id="bBlue" cx=".35" cy=".35"><stop offset="0" stop-color="#7fd2ff"/><stop offset="1" stop-color="#0a6fc4"/></radialGradient>
      <radialGradient id="bPurple" cx=".35" cy=".35"><stop offset="0" stop-color="#9b8ad0"/><stop offset="1" stop-color="#3c2f78"/></radialGradient>
      <radialGradient id="glow"><stop offset=".4" stop-color="#ffe800"/><stop offset="1" stop-color="#ffe800" stop-opacity="0"/></radialGradient>
    </defs>
    <rect x="50" y="10" width="532" height="535" fill="#e4e4e4"/>
    <rect x="50" y="10" width="532" height="535" fill="url(#grid)"/>
    <path d="M582 10V545H50" stroke="#fafafa" fill="none"/>
    <g stroke="#fff" stroke-width="1">
      <path d="M44 10h6M44 54.6h6M44 99.2h6M44 143.8h6M44 188.3h6M44 232.9h6M44 277.5h6M44 322.1h6M44 366.7h6M44 411.3h6M44 455.8h6M44 500.4h6M44 545h6"/>
      <path d="M50 545v6M94.3 545v6M138.7 545v6M183 545v6M227.3 545v6M271.7 545v6M316 545v6M360.3 545v6M404.7 545v6M449 545v6M493.3 545v6M537.7 545v6M582 545v6"/>
    </g>
    <g font-size="9" fill="#fff" text-anchor="end">
      <text x="40" y="13">-12</text><text x="40" y="57.6">-13</text><text x="40" y="102.2">-14</text><text x="40" y="146.8">-15</text><text x="40" y="191.3">-16</text><text x="40" y="235.9">-17</text><text x="40" y="280.5">-18</text><text x="40" y="325.1">-19</text><text x="40" y="369.7">-20</text><text x="40" y="414.3">-21</text><text x="40" y="458.8">-22</text><text x="40" y="503.4">-23</text><text x="40" y="548">-24</text>
    </g>
    <g font-size="9" fill="#fff" text-anchor="middle">
      <text x="48" y="561">-24</text><text x="94.3" y="561">-23</text><text x="138.7" y="561">-22</text><text x="183" y="561">-21</text><text x="227.3" y="561">-20</text><text x="271.7" y="561">-19</text><text x="316" y="561">-18</text><text x="360.3" y="561">-17</text><text x="404.7" y="561">-16</text><text x="449" y="561">-15</text><text x="493.3" y="561">-14</text><text x="537.7" y="561">-13</text><text x="582" y="561">-12</text>
    </g>
    <text x="316" y="538" font-size="8" fill="#333" text-anchor="middle">LOSS</text>
    <text font-size="8" fill="#333" transform="translate(62,333) rotate(-90)">CORRELATION SURPRISE</text>
    <path d="M50 397H194V545" stroke="#d9261c" stroke-width="2" fill="none"/>
    <circle cx="194" cy="397" r="20" fill="url(#glow)"/>
    <circle cx="194" cy="397" r="9" fill="url(#bRed)"/>
    <circle cx="105" cy="491" r="10" fill="url(#glow)" opacity=".5"/>
    <circle cx="105" cy="491" r="8" fill="url(#bOrange)"/>
    <circle cx="439" cy="188" r="8" fill="url(#bBlue)"/>
    <circle cx="472" cy="165" r="8" fill="url(#bPurple)"/>
    <g>
      <rect x="175" y="303" width="216" height="72" rx="4" fill="#fff"/>
      <path d="M175 307a4 4 0 0 1 4-4h208a4 4 0 0 1 4 4v18H175z" fill="#f5c518"/>
      <text x="283" y="319" font-size="13" font-weight="700" text-anchor="middle" fill="#111">STAGFLATION SEVERE</text>
      <g font-size="12.5" font-weight="700" text-anchor="middle" fill="#111">
        <text x="283" y="340">Loss: -18.82</text><text x="283" y="355">Plausibility: 0.00</text><text x="283" y="370">Correlation Surprise: -18.82</text>
      </g>
    </g>
  </svg>

  <section class="bars" style="left:755px;top:111px;width:331px;height:261px;background:#fff;border-radius:5px">
    <div class="bar-title" style="background:linear-gradient(180deg,#8fd04e,#5aa02a)">ASSET CONTRIBUTION 10 HIGHEST</div>
    <svg width="331" height="261" font-family="Arimo,Arial,sans-serif" font-size="10.5">
      <rect x="138" y="30" width="184" height="200" fill="#e6e6e6" stroke="#7cc242"/>
      <g stroke="#fff"><path d="M175 30v200M212 30v200M248 30v200M285 30v200"/></g>
      <g font-weight="700" fill="#111" text-anchor="end">
        <text x="82" y="44">HVR 6.505</text><text x="82" y="64">TKX 6.02</text><text x="82" y="84">FNRB 6.5</text><text x="82" y="104">GV 5.5</text><text x="82" y="124">TRDCN 7.875</text><text x="82" y="144">UNL Float</text><text x="82" y="164">WRM 7.506</text><text x="82" y="184">MANTOR 12.5</text><text x="82" y="204">BYOS 10.25</text><text x="82" y="224">YRC 10.25</text>
      </g>
      <g fill="#111"><text x="88" y="44">02/12/67</text><text x="88" y="64">02/15/67</text><text x="88" y="84">04/15/37</text><text x="88" y="104">12/31/49</text><text x="88" y="124">01/15/19</text><text x="88" y="144">07/02/14</text><text x="88" y="164">05/29/49</text><text x="88" y="184">02/15/18</text><text x="88" y="204">10/01/15</text><text x="88" y="224">02/15/16</text></g>
      <g fill="#7cc242">
        <rect x="138" y="39" width="130" height="3"/><rect x="138" y="59" width="110" height="3"/><rect x="138" y="79" width="70" height="3"/><rect x="138" y="99" width="32" height="3"/><rect x="138" y="119" width="30" height="3"/><rect x="138" y="139" width="17" height="3"/><rect x="138" y="159" width="17" height="3"/><rect x="138" y="179" width="6" height="3"/><rect x="138" y="199" width="6" height="3"/><rect x="138" y="219" width="4" height="3"/>
        <rect x="261" y="34" width="32" height="13" rx="2"/><rect x="241" y="54" width="32" height="13" rx="2"/><rect x="211" y="74" width="32" height="13" rx="2"/><rect x="170" y="94" width="32" height="13" rx="2"/><rect x="168" y="114" width="32" height="13" rx="2"/><rect x="155" y="134" width="32" height="13" rx="2"/><rect x="155" y="154" width="32" height="13" rx="2"/><rect x="143" y="174" width="32" height="13" rx="2"/><rect x="143" y="194" width="32" height="13" rx="2"/><rect x="141" y="214" width="32" height="13" rx="2"/>
      </g>
      <g fill="#fff" text-anchor="middle" font-size="10">
        <text x="277" y="44">0.083</text><text x="257" y="64">0.071</text><text x="227" y="84">0.038</text><text x="186" y="104">0.017</text><text x="184" y="124">0.016</text><text x="171" y="144">0.009</text><text x="171" y="164">0.009</text><text x="159" y="184">0.002</text><text x="159" y="204">0.002</text><text x="157" y="224">0.001</text>
      </g>
      <g font-size="9" fill="#111" text-anchor="middle"><text x="138" y="248">0.00</text><text x="175" y="248">0.02</text><text x="212" y="248">0.04</text><text x="248" y="248">0.06</text><text x="285" y="248">0.08</text><text x="320" y="248">0.10</text></g>
    </svg>
  </section>

  <section class="bars" style="left:755px;top:382px;width:331px;height:261px;background:#fff;border-radius:5px">
    <div class="bar-title" style="background:linear-gradient(180deg,#e6453a,#b41a12)">ASSET CONTRIBUTION 10 LOWEST</div>
    <svg width="331" height="261" font-family="Arimo,Arial,sans-serif" font-size="10.5">
      <rect x="140" y="30" width="182" height="200" fill="#e6e6e6" stroke="#d9261c"/>
      <g stroke="#fff"><path d="M176 30v200M212 30v200M249 30v200M285 30v200"/></g>
      <g font-weight="700" fill="#111" text-anchor="end">
        <text x="82" y="44">WZ 7.375</text><text x="82" y="64">TURKEY 7</text><text x="82" y="84">TII 0.125</text><text x="82" y="104">T 3.125</text><text x="82" y="124">INDON 5.875</text><text x="132" y="144">WAVO 2005-AR6 X</text><text x="82" y="164">RUSSIA 4.5</text><text x="82" y="184">TII 3/875</text><text x="82" y="204">TII 3.875</text><text x="82" y="224">AXIRA 8.6</text>
      </g>
      <g fill="#111"><text x="88" y="44">03/15/32</text><text x="88" y="64">06/05/20</text><text x="88" y="84">01/15/22</text><text x="88" y="104">02/15/43</text><text x="88" y="124">03/13/20</text><text x="88" y="164">04/04/22</text><text x="88" y="184">04/04/22</text><text x="88" y="204">04/15/29</text><text x="88" y="224">12/15/30</text></g>
      <g fill="#d9261c">
        <rect x="140" y="39" width="23" height="3"/><rect x="140" y="59" width="23" height="3"/><rect x="140" y="79" width="25" height="3"/><rect x="140" y="99" width="26" height="3"/><rect x="140" y="119" width="26" height="3"/><rect x="140" y="139" width="26" height="3"/><rect x="140" y="159" width="27" height="3"/><rect x="140" y="179" width="42" height="3"/><rect x="140" y="199" width="66" height="3"/><rect x="140" y="219" width="144" height="3"/>
        <rect x="140" y="34" width="34" height="13" rx="2"/><rect x="140" y="54" width="34" height="13" rx="2"/><rect x="140" y="74" width="34" height="13" rx="2"/><rect x="140" y="94" width="34" height="13" rx="2"/><rect x="140" y="114" width="34" height="13" rx="2"/><rect x="140" y="134" width="34" height="13" rx="2"/><rect x="140" y="154" width="34" height="13" rx="2"/><rect x="167" y="174" width="34" height="13" rx="2"/><rect x="190" y="194" width="34" height="13" rx="2"/><rect x="269" y="214" width="34" height="13" rx="2"/>
      </g>
      <g fill="#fff" text-anchor="middle" font-size="10">
        <text x="157" y="44">-0.320</text><text x="157" y="64">-0.322</text><text x="157" y="84">-0.343</text><text x="157" y="104">-0.352</text><text x="157" y="124">-0.354</text><text x="157" y="144">-0.360</text><text x="157" y="164">-0.370</text><text x="184" y="184">-0.577</text><text x="207" y="204">-0.900</text><text x="286" y="224">-1.975</text>
      </g>
      <g font-size="9" fill="#111" text-anchor="middle"><text x="140" y="248">0.0</text><text x="176" y="248">-0.5</text><text x="212" y="248">-1.0</text><text x="249" y="248">-1.5</text><text x="285" y="248">-2.0</text><text x="320" y="248">-2.5</text></g>
    </svg>
  </section>

  <section class="table" style="left:16px;width:528px">
    <div class="table-title">SHOCKS</div>
    <div class="row head"><span class="cell" style="width:230px;border:0">Name</span><span class="cell" style="width:196px;border:0;padding-left:56px">Type</span><span class="cell num" style="width:102px;border:0;padding-right:28px">Shock</span></div>
    <div class="row"><span class="cell" style="width:230px">United States</span><span class="cell mid" style="width:196px">Equity Indexx</span><span class="cell num" style="width:102px;border:0;padding-right:38px">-15</span></div>
    <div class="row alt"><span class="cell" style="width:230px">Gold</span><span class="cell mid" style="width:196px">Macro/Styxxx</span><span class="cell num" style="width:102px;border:0;padding-right:38px">60</span></div>
    <div class="row"><span class="cell" style="width:230px">3 Years US Government</span><span class="cell mid" style="width:196px">Interest Ratxx</span><span class="cell num" style="width:102px;border:0;padding-right:38px">3</span></div>
    <div class="row alt"><span class="cell" style="width:230px">30 Years US Government</span><span class="cell mid" style="width:196px">Interest Ratxx</span><span class="cell num" style="width:102px;border:0;padding-right:38px">3</span></div>
  </section>

  <section class="table" style="left:557px;width:529px">
    <div class="table-title" style="position:relative">CURRENT SCENARIO
      <svg width="50" height="18" style="position:absolute;right:12px;top:4px"><circle cx="9" cy="9" r="8" fill="#7cc242"/><path d="M9 4v10M4 9h10" stroke="#fff" stroke-width="2.5"/><circle cx="40" cy="9" r="8" fill="#e02b20"/><path d="M35 9h10" stroke="#fff" stroke-width="2.5"/></svg>
    </div>
    <div class="row head"><span class="cell" style="width:188px;border:0">Name</span><span class="cell mid" style="width:96px;border:0">Loss</span><span class="cell mid" style="width:132px;border:0">Correlation</span><span class="cell" style="width:113px;border:0">Planxxxx</span></div>
    <div class="row"><span class="cell" style="width:188px">US Treasury Interest</span><span class="cell mid" style="width:96px">-21.57</span><span class="cell mid" style="width:132px">-21.57</span><span class="cell" style="width:113px;border:0"></span></div>
    <div class="row selected"><span class="cell" style="width:188px">Stagflation Severe</span><span class="cell mid" style="width:96px">-18.82</span><span class="cell mid" style="width:132px">-18.82</span><span class="cell" style="width:113px;border:0"></span></div>
    <div class="row"><span class="cell" style="width:188px">Stagflation</span><span class="cell mid" style="width:96px">-11.1</span><span class="cell mid" style="width:132px">-11.1</span><span class="cell" style="width:113px;border:0"></span></div>
    <div class="row alt"><span class="cell" style="width:188px">US Treasury Interest</span><span class="cell mid" style="width:96px">-10.87</span><span class="cell mid" style="width:132px">-10.87</span><span class="cell" style="width:113px;border:0"></span></div>
  </section>
</main>
</body>
</html>
```